Heater product information sheets

I need the two product information sheets organized and laid out in a clean, easy to read attractive manner. These sheets are to advertise propane heaters for outdoor use and for wholesale to propane distributors, restaurants and homeowners that need to have propane heat as the winter ends and spring begins. They will be used for chilly evenings when people want to be outside eating, drinking and being social.
Updates

Low design quality

Target Market(s)

Restaurants, hospitality industry, special events, party rental companies, home owners with backyards

Font styles to use
Sans Serif

Requirements
Must have
• My logo in the document instead of k. Dahlby and company
Nice to have
• I would like to see Fire illustrated coming up the heaters and on the round glass, show it up the middle of the glass tube propane heater.

```html
<!DOCTYPE html>
<html lang="en">
<head>
<meta charset="utf-8">
<title>Propane Heater Product Sheets</title>
<link href="https://fonts.googleapis.com/css2?family=Oswald:wght@600&family=Roboto:wght@400;500;700&family=Roboto+Condensed:wght@700&display=swap" rel="stylesheet">
<style>
:root{
  --bg:#e9e9e9;
  --paper:#ffffff;
  --ink:#2a2a2a;
  --dark:#1a0f0c;
  --red:#e3242b;
  --blue:#2a2f8f;
  --orange:#f08a1c;
  --orange-deep:#e2701a;
  --dot:#d9d9d9;
}
*{margin:0;padding:0;box-sizing:border-box}
html,body{width:1200px;height:900px;overflow:hidden;background:var(--bg)}
body{position:relative;font-family:"Roboto",Arial,sans-serif;color:var(--ink)}
.sheet{position:absolute;top:88px;width:540px;height:725px;background:var(--paper);overflow:hidden;box-shadow:0 2px 10px rgba(0,0,0,.18)}
.sheet--glass{left:40px}
.sheet--outdoor{left:620px}
.sheet__art{position:absolute;left:0;top:0}
.brand{position:absolute;left:40px;top:22px;color:#fff}
.brand__name{font-family:"Roboto",Arial,sans-serif;font-weight:700;font-size:44px;letter-spacing:-2px;line-height:1}
.brand__tag{font-size:10px;margin-top:4px;font-weight:400}
.sheet__title{position:absolute;left:28px;top:92px;font-family:"Oswald",Arial,sans-serif;font-weight:600;font-size:42px;line-height:1.12;color:#fff}
.product{position:absolute}
.sheet--glass .product{left:55px;top:218px;width:130px;height:330px}
.sheet--outdoor .product{left:70px;top:218px;width:150px;height:340px}
.specs{position:absolute;left:305px;top:307px;width:230px}
.specs__heading{font-family:"Roboto Condensed",Arial,sans-serif;font-weight:700;font-size:13px;color:var(--red);margin-bottom:3px}
.specs__heading + .specs__list{margin-bottom:12px}
.specs__list{list-style:none}
.specs__list li{position:relative;padding-left:14px;font-size:10.5px;line-height:13px;margin-bottom:2.7px}
.specs__list li::before{content:"";position:absolute;left:1px;top:4px;width:5px;height:5px;border-radius:50%;background:var(--orange)}
.services{position:absolute;left:30px;top:572px;list-style:none}
.service{display:flex;align-items:center;margin-bottom:8px}
.service__icon{width:26px;height:26px;margin-right:12px;flex:none}
.service__label{width:198px;min-height:24px;padding:4px 8px;border-radius:5px;background:var(--red);color:#fff;font-family:"Roboto Condensed",Arial,sans-serif;font-weight:700;font-size:12px;line-height:11px;letter-spacing:.3px;display:flex;align-items:center;box-shadow:0 2px 2px rgba(0,0,0,.25)}
.note{position:absolute;left:318px;top:626px;width:188px;height:30px;border:1px solid #999;border-radius:3px;display:flex;align-items:center;background:#fff}
.note__tag{width:38px;height:100%;background:#ddd;font-size:7px;font-weight:700;font-style:italic;display:flex;align-items:center;justify-content:center}
.note__text{font-size:5.6px;line-height:7px;font-style:italic;padding-left:8px}
.footer{position:absolute;left:0;bottom:0;width:540px;height:70px}
.footer__art{position:absolute;left:0;top:0}
.footer__cta{position:absolute;left:180px;top:34px;color:#fff;font-size:9px;font-style:italic;font-weight:500}
.contact{position:absolute;left:312px;top:6px;color:#fff}
.contact__name{font-size:12.5px;font-weight:500;margin-bottom:9px}
.contact__row{display:flex;align-items:center;font-size:8.5px;margin-bottom:4px;color:var(--dark)}
.contact__row span{display:inline-flex;align-items:center;margin-right:8px}
.contact__row svg{width:8px;height:8px;margin-right:4px}
</style>
</head>
<body>

<!-- Glass tube heater sheet -->
<section class="sheet sheet--glass">
  <svg class="sheet__art" width="540" height="725" viewBox="0 0 540 725">
    <defs>
      <pattern id="dotsA" width="6" height="6" patternUnits="userSpaceOnUse"><circle cx="1" cy="1" r=".7" fill="#d6d6d6"/></pattern>
      <radialGradient id="glowA" cx="78%" cy="38%" r="55%"><stop offset="0" stop-color="#c56a1c"/><stop offset=".45" stop-color="#5a2a12"/><stop offset="1" stop-color="#160c0a"/></radialGradient>
      <linearGradient id="stripeA" x1="0" x2="1"><stop offset="0" stop-color="#2a2f8f"/><stop offset=".35" stop-color="#3b2f96"/><stop offset=".7" stop-color="#8a2a7a"/><stop offset="1" stop-color="#e3242b"/></linearGradient>
    </defs>
    <polygon points="0,250 150,340 540,225 540,640 0,640" fill="url(#dotsA)"/>
    <polygon points="0,232 150,306 540,214 540,248 150,344 0,262" fill="url(#stripeA)"/>
    <polygon points="0,0 540,0 540,214 150,306 0,232" fill="url(#glowA)" role="img" aria-label="Photo of a lit patio heater flame with warm bokeh lights"/>
  </svg>
  <div class="brand"><div class="brand__name">NWPR</div><div class="brand__tag">Northwind Party Rental</div></div>
  <h1 class="sheet__title">Glass Tube<br>Propane Heaters</h1>
  <svg class="product" viewBox="0 0 130 330" role="img" aria-label="Product photo of a black glass tube propane heater">
    <defs><linearGradient id="prodA" x1="0" y1="0" x2="0" y2="1"><stop offset="0" stop-color="#c9c9c9"/><stop offset=".5" stop-color="#8a8a8a"/><stop offset="1" stop-color="#151515"/></linearGradient></defs>
    <rect x="5" y="0" width="120" height="330" rx="14" fill="url(#prodA)"/>
  </svg>
  <div class="specs">
    <h2 class="specs__heading">SPECIFICATIONS</h2>
    <ul class="specs__list">
      <li>Powerful 48,000 BTU</li>
      <li>Black Powder Coated Finish</li>
      <li>Uses 20 lbs. Propane Tank</li>
      <li>CE, GS, AGA, CSA, with ETL certificate and ROHS approved.</li>
    </ul>
    <h2 class="specs__heading">ADDITIONAL DETAILS</h2>
    <ul class="specs__list">
      <li>Commercial Quality</li>
      <li>For Outdoor Use Only</li>
      <li>Conforms to ANSI STD Z83.26-2014 Certified to CSA STD 2.37-2014 Gas-fired outdoor infrared patio heaters</li>
      <li>Safety Auto Shut Off Switch</li>
      <li>Thermostatic Control</li>
      <li>Base Diameter 17" - Anti-Tip Design</li>
      <li>Standard Wheels - Tilt &amp; Move</li>
      <li>Run time: 8-10 hours with standard 20 lbs.</li>
      <li>Propane tank 96" Tall</li>
      <li>Heating Area: 200 sq. ft</li>
    </ul>
  </div>
  <ul class="services">
    <li class="service"><svg class="service__icon" viewBox="0 0 26 26"><circle cx="13" cy="13" r="12" fill="var(--red)"/><circle cx="13" cy="13" r="9" fill="none" stroke="#fff" stroke-width="1.5"/><circle cx="13" cy="9" r="2" fill="#fff"/><rect x="11" y="12" width="4" height="7" fill="#fff"/></svg><span class="service__label">RENTALS FOR LIVE EVENTS</span></li>
    <li class="service"><svg class="service__icon" viewBox="0 0 26 26"><circle cx="13" cy="13" r="12" fill="var(--red)"/><circle cx="13" cy="13" r="9" fill="none" stroke="#fff" stroke-width="1.5"/><path d="M8 13 L13 8 L18 13 V18 H8 Z" fill="#fff"/></svg><span class="service__label">RENTALS FOR RESTAURANTS<br>&amp; CATERING HALLS</span></li>
    <li class="service"><svg class="service__icon" viewBox="0 0 26 26"><circle cx="13" cy="13" r="12" fill="var(--red)"/><circle cx="13" cy="13" r="9" fill="none" stroke="#fff" stroke-width="1.5"/><path d="M7 13 L13 7 L19 13 M9 12 V18 H17 V12" fill="none" stroke="#fff" stroke-width="1.8"/></svg><span class="service__label">PURCHASE FOR YOUR HOME<br>OR BUSINESS</span></li>
  </ul>
  <footer class="footer">
    <svg class="footer__art" width="540" height="70" viewBox="0 0 540 70">
      <polygon points="0,30 300,30 290,48 0,48" fill="var(--blue)"/>
      <polygon points="0,48 290,48 282,66 0,66" fill="var(--red)"/>
      <polygon points="300,0 540,0 540,70 270,70" fill="var(--orange)"/>
      <polygon points="300,0 540,0 540,22 292,22" fill="var(--orange-deep)"/>
    </svg>
    <span class="footer__cta">To Rent or Purchase:</span>
    <div class="contact">
      <div class="contact__name">K. Dahlby &amp; Company</div>
      <div class="contact__row"><span><svg viewBox="0 0 8 8"><circle cx="4" cy="4" r="4" fill="#1a0f0c"/></svg>555-014-2290</span><span><svg viewBox="0 0 8 8"><circle cx="4" cy="4" r="4" fill="#1a0f0c"/></svg>mara@northwindrental.com</span></div>
      <div class="contact__row"><span><svg viewBox="0 0 8 8"><path d="M4 0a3 3 0 0 1 3 3c0 2-3 5-3 5S1 5 1 3a3 3 0 0 1 3-3z" fill="#1a0f0c"/></svg>42 Mill Street Riverton, NJ 08077</span></div>
    </div>
  </footer>
</section>

<!-- Outdoor heater sheet -->
<section class="sheet sheet--outdoor">
  <svg class="sheet__art" width="540" height="725" viewBox="0 0 540 725">
    <defs>
      <pattern id="dotsB" width="6" height="6" patternUnits="userSpaceOnUse"><circle cx="1" cy="1" r=".7" fill="#d6d6d6"/></pattern>
      <radialGradient id="glowB" cx="78%" cy="38%" r="55%"><stop offset="0" stop-color="#c56a1c"/><stop offset=".45" stop-color="#5a2a12"/><stop offset="1" stop-color="#160c0a"/></radialGradient>
      <linearGradient id="stripeB" x1="0" x2="1"><stop offset="0" stop-color="#2a2f8f"/><stop offset=".35" stop-color="#3b2f96"/><stop offset=".7" stop-color="#8a2a7a"/><stop offset="1" stop-color="#e3242b"/></linearGradient>
    </defs>
    <polygon points="0,250 150,340 540,225 540,640 0,640" fill="url(#dotsB)"/>
    <polygon points="0,232 150,306 540,214 540,248 150,344 0,262" fill="url(#stripeB)"/>
    <polygon points="0,0 540,0 540,214 150,306 0,232" fill="url(#glowB)" role="img" aria-label="Photo of a lit patio heater flame with warm bokeh lights"/>
  </svg>
  <div class="brand"><div class="brand__name">NWPR</div><div class="brand__tag">Northwind Party Rental</div></div>
  <h1 class="sheet__title">Outdoor<br>Propane Heater</h1>
  <svg class="product" viewBox="0 0 150 340" role="img" aria-label="Product photo of a black mushroom-top outdoor propane heater">
    <defs><linearGradient id="prodB" x1="0" y1="0" x2="0" y2="1"><stop offset="0" stop-color="#cfcfcf"/><stop offset=".4" stop-color="#6d6d6d"/><stop offset="1" stop-color="#121212"/></linearGradient></defs>
    <rect x="5" y="0" width="140" height="340" rx="16" fill="url(#prodB)"/>
  </svg>
  <div class="specs">
    <h2 class="specs__heading">SPECIFICATIONS</h2>
    <ul class="specs__list">
      <li>Powerful 48,000 BTU</li>
      <li>Black Powder Coated Finish</li>
      <li>Uses 20 lbs. Propane Tank</li>
      <li>CE, GS, AGA, CSA, with ETL certificate and ROHS approved.</li>
    </ul>
    <h2 class="specs__heading">ADDITIONAL DETAILS</h2>
    <ul class="specs__list">
      <li>Commercial Quality</li>
      <li>For Outdoor Use Only</li>
      <li>Conforms to ANSI STD Z83.26-2014 Certified to CSA STD 2.37-2014 Gas-fired outdoor infrared patio heaters</li>
      <li>Safety Auto Shut Off Switch</li>
      <li>Thermostatic Control</li>
      <li>Base Diameter 17" - Anti-Tip Design</li>
      <li>Standard Wheels - Tilt &amp; Move</li>
      <li>Run time: 8-10 hours with standard 20 lbs.</li>
      <li>Propane tank 88" Tall</li>
      <li>Heating Area: 200 sq. ft</li>
    </ul>
  </div>
  <div class="note">
    <span class="note__tag">NOTE</span>
    <p class="note__text">Price: Starting at $250 each<br>Assembly &amp; Delivery available upon request.<br>Discounts for large quantity orders</p>
  </div>
  <ul class="services">
    <li class="service"><svg class="service__icon" viewBox="0 0 26 26"><circle cx="13" cy="13" r="12" fill="var(--red)"/><circle cx="13" cy="13" r="9" fill="none" stroke="#fff" stroke-width="1.5"/><circle cx="13" cy="9" r="2" fill="#fff"/><rect x="11" y="12" width="4" height="7" fill="#fff"/></svg><span class="service__label">RENTALS FOR LIVE EVENTS</span></li>
    <li class="service"><svg class="service__icon" viewBox="0 0 26 26"><circle cx="13" cy="13" r="12" fill="var(--red)"/><circle cx="13" cy="13" r="9" fill="none" stroke="#fff" stroke-width="1.5"/><path d="M8 13 L13 8 L18 13 V18 H8 Z" fill="#fff"/></svg><span class="service__label">RENTALS FOR RESTAURANTS<br>&amp; CATERING HALLS</span></li>
    <li class="service"><svg class="service__icon" viewBox="0 0 26 26"><circle cx="13" cy="13" r="12" fill="var(--red)"/><circle cx="13" cy="13" r="9" fill="none" stroke="#fff" stroke-width="1.5"/><path d="M7 13 L13 7 L19 13 M9 12 V18 H17 V12" fill="none" stroke="#fff" stroke-width="1.8"/></svg><span class="service__label">PURCHASE FOR YOUR HOME<br>OR BUSINESS</span></li>
  </ul>
  <footer class="footer">
    <svg class="footer__art" width="540" height="70" viewBox="0 0 540 70">
      <polygon points="0,30 300,30 290,48 0,48" fill="var(--blue)"/>
      <polygon points="0,48 290,48 282,66 0,66" fill="var(--red)"/>
      <polygon points="300,0 540,0 540,70 270,70" fill="var(--orange)"/>
      <polygon points="300,0 540,0 540,22 292,22" fill="var(--orange-deep)"/>
    </svg>
    <span class="footer__cta">To Rent or Purchase:</span>
    <div class="contact">
      <div class="contact__name">K. Dahlby &amp; Company</div>
      <div class="contact__row"><span><svg viewBox="0 0 8 8"><circle cx="4" cy="4" r="4" fill="#1a0f0c"/></svg>555-014-2290</span><span><svg viewBox="0 0 8 8"><circle cx="4" cy="4" r="4" fill="#1a0f0c"/></svg>mara@northwindrental.com</span></div>
      <div class="contact__row"><span><svg viewBox="0 0 8 8"><path d="M4 0a3 3 0 0 1 3 3c0 2-3 5-3 5S1 5 1 3a3 3 0 0 1 3-3z" fill="#1a0f0c"/></svg>42 Mill Street Riverton, NJ 08077</span></div>
    </div>
  </footer>
</section>

</body>
</html>
```